Brindova Electrical Solutions needs a website

We need a new website designed because our current one is outdated. I would like a one-page website. We are a B2B company and want to maintain a professional appearance to appeal to project managers and directors.

for some reference, these are a few of my competitor's websites; we offer the same services.

https://valtrawire.com.au/services
https://www.drumwell.com.au/mechanical-electrical-services/
https://www.qulan.com.au/

Industry/Entity Type

Electrical

Number of Pages Required

1 page

Font styles to use
Sans Serif

Colors
0054AA
0677BA
7BADD7
CADEEF
E8F1F8

```html
<!DOCTYPE html>
<html lang="en">
<head>
<meta charset="utf-8">
<title>Brindova Electrical Solutions</title>
<link href="https://fonts.googleapis.com/css2?family=Poppins:wght@400;500;600;700&family=Lexend:wght@600;700&display=swap" rel="stylesheet">
<style>
:root{
  --blue:#0a8fd1;
  --blue-dark:#0054aa;
  --blue-mid:#0677ba;
  --blue-soft:#7badd7;
  --blue-pale:#cadeef;
  --blue-mist:#e8f1f8;
  --ink:#111;
  --text:#333;
  --white:#fff;
  --footer:#000;
}
*{margin:0;padding:0;box-sizing:border-box}
html,body{width:1200px;height:3176px;overflow:hidden}
body{font-family:"Poppins",sans-serif;color:var(--text);background:var(--white);position:relative}
section,header,footer{position:absolute;left:0;width:1200px}
.abs{position:absolute}
.btn{position:absolute;display:flex;align-items:center;justify-content:center;border-radius:30px;font-weight:500;font-size:14px}
.btn-solid{background:var(--blue);color:var(--white)}
.btn-ghost{border:1.5px solid var(--white);color:var(--white)}
.btn-outline{border:1.5px solid var(--ink);color:var(--ink)}
.section-title{font-family:"Lexend",sans-serif;font-weight:700;letter-spacing:1px;text-transform:uppercase;color:var(--ink)}

/* header */
.site-header{top:0;height:89px;background:var(--white)}
.brand{left:55px;top:25px;display:flex;align-items:center;gap:12px}
.brand-dot{width:36px;height:36px;border-radius:50%;background:var(--blue-dark)}
.brand-name{font-weight:600;font-size:22px;color:var(--blue-dark)}
.nav{left:378px;top:35px;display:flex;gap:24px;font-weight:600;font-size:15px;color:var(--ink);text-transform:uppercase}
.nav .active{color:var(--blue)}
.socials{right:56px;top:30px;display:flex;gap:10px}
.socials span{width:30px;height:30px;border-radius:50%;background:var(--blue)}

/* hero */
.hero{top:89px;height:470px}
.hero-photo{position:absolute;inset:0;background:linear-gradient(100deg,#16303f 0%,#1d4a5e 45%,#2d6f85 70%,#133445 100%)}
.hero h1{left:57px;top:115px;font-weight:700;font-size:53px;line-height:64px;color:var(--white)}
.hero p{left:57px;top:250px;width:530px;font-size:13px;line-height:19px;color:var(--white)}
.dots{left:572px;top:430px;display:flex;gap:4px}
.dots span{width:14px;height:3px;background:var(--white);border-radius:2px}
.dots span:first-child{background:var(--blue)}

/* about */
.about{top:559px;height:450px}
.about-photo{left:57px;top:61px;width:528px;height:325px;border-radius:6px;background:linear-gradient(180deg,#8fb4d6 0%,#c9d4d8 40%,#5a7a80 60%,#2c5a6e 100%)}
.about h2{left:660px;top:80px;font-size:36px}
.about .copy{left:658px;top:148px;width:490px;font-size:12.6px;line-height:19px;color:var(--ink)}
.about .copy p+p{margin-top:18px}

/* services */
.services{top:1009px;height:560px}
.services-photo{position:absolute;inset:0;background:linear-gradient(180deg,#5a6f7a 0%,#4f6a78 40%,#2f5166 70%,#8a7a5c 100%)}
.services h2{left:0;width:1200px;text-align:center;top:52px;font-size:36px;color:var(--white)}
.service-card{top:127px;width:353px;height:366px;background:var(--white);border-radius:4px;text-align:center}
.service-icon{position:absolute;left:120px;top:62px;width:113px;height:113px;border-radius:50%;background:var(--blue-mist);display:flex;align-items:center;justify-content:center}
.service-card h3{position:absolute;left:0;width:100%;top:196px;font-size:17px;font-weight:600;letter-spacing:.5px;color:var(--ink)}
.service-card.featured h3{color:var(--blue)}
.service-card p{position:absolute;left:55px;width:243px;top:229px;font-size:12.4px;line-height:17px;color:var(--ink)}
.service-card .btn{left:23px;top:302px;width:307px;height:37px;font-size:14px}

/* projects */
.projects{top:1569px;height:850px}
.projects h2{left:57px;top:57px;font-size:36px}
.arrow-btn{top:50px;width:42px;height:42px;border-radius:50%;display:flex;align-items:center;justify-content:center}
.arrow-prev{left:1047px;border:1px solid #ddd;background:var(--white)}
.arrow-next{left:1097px;background:var(--blue)}
.project{overflow:hidden;border-radius:3px}
.project .fill{position:absolute;inset:0}
.project .shade{position:absolute;inset:0;background:linear-gradient(180deg,rgba(0,0,0,0) 55%,rgba(0,0,0,.55) 100%)}
.project h4{position:absolute;left:38px;font-size:17px;font-weight:600;color:var(--white)}
.project p{position:absolute;left:40px;bottom:37px;width:530px;font-size:12.4px;line-height:19px;color:var(--white)}
.open{position:absolute;top:17px;right:17px;width:46px;height:46px;border-radius:50%;background:var(--white);display:flex;align-items:center;justify-content:center}
.open.on{background:var(--blue)}

/* message */
.message{top:2419px;height:487px}
.message-photo{position:absolute;inset:0;background:linear-gradient(90deg,#3a3f3a 0%,#25292b 40%,#1e2226 70%,#30332f 100%)}
.message h2{left:0;width:1200px;text-align:center;top:42px;font-size:36px;color:var(--white)}
.message .lead{left:0;width:1200px;text-align:center;top:96px;font-size:12.6px;color:var(--white)}
.field{background:var(--white);border-radius:20px;font-size:12.6px;color:#888;padding:0 16px;display:flex;align-items:center}
.field.area{align-items:flex-start;padding-top:18px;border-radius:10px;font-size:14px}
.send{left:161px;top:399px;width:891px;height:37px;font-size:14px}

/* footer */
.site-footer{top:2906px;height:270px;background:var(--footer);color:var(--white)}
.footer-brand{left:55px;top:50px;display:flex;align-items:center;gap:14px}
.footer-brand .brand-dot{width:76px;height:76px;background:var(--white)}
.footer-brand .brand-name{color:var(--white);font-size:30px}
.footer-about{left:56px;top:152px;width:345px;font-size:12.6px;line-height:19px}
.footer-h{font-size:14px;font-weight:600;color:var(--blue)}
.links{left:612px;top:44px}
.links ul{margin-top:12px;list-style:none;font-size:12.6px;line-height:24px}
.links li::before{content:"•";margin-right:8px}
.contact{left:922px;top:38px}
.contact .row{display:flex;align-items:center;gap:8px;font-size:12.6px;margin-top:18px}
.contact .ico{width:21px;height:21px;border-radius:50%;background:var(--white);display:flex;align-items:center;justify-content:center}
.rule{left:0;top:221px;width:1200px;height:1px;background:#666}
.legal{top:238px;font-size:12.6px}
</style>
</head>
<body>

<header class="site-header">
  <div class="abs brand"><span class="brand-dot"></span><span class="brand-name">Brindova</span></div>
  <nav class="abs nav"><span class="active">Home</span><span>About Us</span><span>Services</span><span>Latest Projects</span><span>Contact</span></nav>
  <div class="abs socials" aria-label="Social links"><span></span><span></span><span></span></div>
</header>

<section class="hero">
  <div class="hero-photo" role="img" aria-label="Hands on a laptop with glowing sustainable technology icons overlaid"></div>
  <h1 class="abs">Brindova Powering a<br>Sustainable Future</h1>
  <p class="abs">Lorem ipsum dolor sit amet, consectetuer adipiscing elit, sed diam nonummy nibh euismod tincidunt ut laoreet dolore magna aliquam erat volutpat.</p>
  <span class="btn btn-solid" style="left:58px;top:305px;width:136px;height:37px">View our Projects</span>
  <span class="btn btn-ghost" style="left:219px;top:305px;width:116px;height:37px">Learn More</span>
  <div class="abs dots"><span></span><span></span><span></span></div>
</section>

<section class="about">
  <div class="abs about-photo" role="img" aria-label="Sydney harbour skyline with the opera house at sunset"></div>
  <h2 class="abs section-title">About Us</h2>
  <div class="abs copy">
    <p>Lorem ipsum dolor sit amet, consectetuer adipiscing elit, sed diam nonummy nibh euismod tincidunt ut laoreet dolore magna aliquam erat volutpat. Ut wisi enim ad minim veniam, quis nostrud exerci tation ullamcorper suscipit lobortis nisl ut aliquip ex ea commodo consequat.</p>
    <p>Duis autem vel eum iriure dolor in hendrerit in vulputate velit esse molestie consequat, vel illum dolore eu feugiat nulla facilisis at vero eros et accumsan et iusto odio dignissim qui blandit praesent luptatum zzril delenit augue duis dolore te feugait nulla facilisi.</p>
  </div>
  <span class="btn btn-solid" style="left:659px;top:333px;width:124px;height:37px">Learn More</span>
</section>

<section class="services">
  <div class="services-photo" role="img" aria-label="Aerial view of a harbour bridge and city suburbs"></div>
  <h2 class="abs section-title">Our Services</h2>

  <div class="abs service-card featured" style="left:57px">
    <div class="service-icon"><svg width="62" height="62" viewBox="0 0 62 62" fill="none" stroke="#0677ba" stroke-width="2"><path d="M8 30 31 10l23 20"/><path d="M14 26v26h34V26"/><rect x="26" y="36" width="10" height="16"/><rect x="38" y="32" width="7" height="7"/><path d="M18 12v8M22 12v5"/><path d="M4 54h54"/></svg></div>
    <h3>RESIDENTIAL SERVICES</h3>
    <p>Lorem ipsum dolor sit amet, consectetuer adipiscing elit, sed diam nonummy nibh euismod tincidunt ut laoreet dolore</p>
    <span class="btn btn-solid">View All Services</span>
  </div>

  <div class="abs service-card" style="left:424px">
    <div class="service-icon"><svg width="62" height="62" viewBox="0 0 62 62" fill="none" stroke="#0677ba" stroke-width="2"><rect x="18" y="10" width="18" height="42"/><rect x="36" y="22" width="10" height="30"/><path d="M22 16h2M28 16h2M22 22h2M28 22h2M22 28h2M28 28h2M22 34h2M28 34h2M22 40h2M28 40h2M40 28h2M40 34h2M40 40h2"/><path d="M6 52h50"/></svg></div>
    <h3>COMMERCIAL SERVICES</h3>
    <p>Lorem ipsum dolor sit amet, consectetuer adipiscing elit, sed diam nonummy nibh euismod tincidunt ut laoreet dolore</p>
    <span class="btn btn-outline">View All Services</span>
  </div>

  <div class="abs service-card" style="left:792px">
    <div class="service-icon"><svg width="62" height="62" viewBox="0 0 62 62" fill="none" stroke="#0677ba" stroke-width="2"><path d="M8 52V30l12-6v6l12-6v6l12-6V52"/><rect x="44" y="10" width="6" height="42"/><rect x="36" y="16" width="5" height="12"/><rect x="14" y="36" width="6" height="5"/><rect x="24" y="36" width="6" height="5"/><rect x="34" y="36" width="6" height="5"/><rect x="14" y="44" width="6" height="5"/><rect x="24" y="44" width="6" height="5"/><path d="M4 52h54"/></svg></div>
    <h3>INDUSTRIAL SERVICES</h3>
    <p>Lorem ipsum dolor sit amet, consectetuer adipiscing elit, sed diam nonummy nibh euismod tincidunt ut laoreet dolore</p>
    <span class="btn btn-outline">View All Services</span>
  </div>
</section>

<section class="projects">
  <h2 class="abs section-title">Latest Projects</h2>
  <span class="abs arrow-btn arrow-prev"><svg width="18" height="12" viewBox="0 0 18 12" fill="none" stroke="#111" stroke-width="1.6"><path d="M17 6H2M6 1 1 6l5 5"/></svg></span>
  <span class="abs arrow-btn arrow-next"><svg width="18" height="12" viewBox="0 0 18 12" fill="none" stroke="#fff" stroke-width="1.6"><path d="M1 6h15M12 1l5 5-5 5"/></svg></span>

  <div class="abs project" style="left:57px;top:135px;width:637px;height:322px">
    <div class="fill" role="img" aria-label="Architectural building model over technical plan sketches" style="background:linear-gradient(120deg,#e6e8ea 0%,#c7cacd 45%,#8e857e 70%,#b9bcbf 100%)"></div>
    <div class="shade"></div>
    <span class="open on"><svg width="16" height="16" viewBox="0 0 16 16" fill="none" stroke="#fff" stroke-width="1.6"><path d="M2 14 14 2M6 2h8v8"/></svg></span>
    <h4 style="bottom:82px">Project Design</h4>
    <p>Lorem ipsum dolor sit amet, consectetuer adipiscing elit, sed diam nonummy nibh euismod tincidunt ut laoreet dolore magna aliquam erat volutpat.</p>
  </div>

  <div class="abs project" style="left:707px;top:135px;width:437px;height:322px">
    <div class="fill" role="img" aria-label="Team reviewing blueprints on a desk" style="background:linear-gradient(135deg,#1e3a5c 0%,#3b5f86 45%,#6c8fae 70%,#2a4666 100%)"></div>
    <div class="shade"></div>
    <span class="open"><svg width="16" height="16" viewBox="0 0 16 16" fill="none" stroke="#111" stroke-width="1.6"><path d="M2 14 14 2M6 2h8v8"/></svg></span>
    <h4 style="left:34px;bottom:36px">Project Management</h4>
  </div>

  <div class="abs project" style="left:58px;top:468px;width:297px;height:322px">
    <div class="fill" role="img" aria-label="Technician testing an electrical switchboard" style="background:linear-gradient(160deg,#c9b89a 0%,#6f6a64 40%,#3f3f44 70%,#8a8d92 100%)"></div>
    <div class="shade"></div>
    <span class="open"><svg width="16" height="16" viewBox="0 0 16 16" fill="none" stroke="#111" stroke-width="1.6"><path d="M2 14 14 2M6 2h8v8"/></svg></span>
    <h4 style="bottom:30px">Engineering</h4>
  </div>

  <div class="abs project" style="left:367px;top:468px;width:406px;height:322px">
    <div class="fill" role="img" aria-label="Modern multi-storey apartment building" style="background:linear-gradient(180deg,#6f9ac8 0%,#a8b8c8 30%,#5b6570 60%,#7c8a6a 85%,#9a9a98 100%)"></div>
    <div class="shade"></div>
    <span class="open"><svg width="16" height="16" viewBox="0 0 16 16" fill="none" stroke="#111" stroke-width="1.6"><path d="M2 14 14 2M6 2h8v8"/></svg></span>
    <h4 style="left:42px;bottom:30px">Commercial</h4>
  </div>

  <div class="abs project" style="left:785px;top:468px;width:359px;height:322px">
    <div class="fill" role="img" aria-label="Technician commissioning a switchboard with a meter" style="background:linear-gradient(160deg,#c9b89a 0%,#6f6a64 40%,#3f3f44 70%,#8a8d92 100%)"></div>
    <div class="shade"></div>
    <span class="open"><svg width="16" height="16" viewBox="0 0 16 16" fill="none" stroke="#111" stroke-width="1.6"><path d="M2 14 14 2M6 2h8v8"/></svg></span>
    <h4 style="left:40px;bottom:34px">Commissioning</h4>
  </div>
</section>

<section class="message">
  <div class="message-photo" role="img" aria-label="Dim office interior with a person on a phone"></div>
  <h2 class="abs section-title">Message Us</h2>
  <p class="abs lead">Please complete the Contact Form and we'll be in touch</p>
  <div class="abs field" style="left:161px;top:137px;width:891px;height:37px">Your Name</div>
  <div class="abs field" style="left:161px;top:189px;width:443px;height:37px">Phone .No</div>
  <div class="abs field" style="left:612px;top:189px;width:443px;height:37px">E - Mail</div>
  <div class="abs field area" style="left:161px;top:242px;width:891px;height:142px">Message...</div>
  <span class="btn btn-solid send">Send Message</span>
</section>

<footer class="site-footer">
  <div class="abs footer-brand"><span class="brand-dot"></span><span class="brand-name">Brindova</span></div>
  <p class="abs footer-about">Lorem ipsum dolor sit amet, consectetuer adipiscing elit, sed diam nonummy nibh euismod tincidunt</p>
  <div class="abs links">
    <div class="footer-h">Quick Links</div>
    <ul><li>Home</li><li>About us</li><li>Services</li><li>Latest Projects</li><li>Contact</li></ul>
  </div>
  <div class="abs contact">
    <div class="footer-h">Contact</div>
    <div class="row"><span class="ico"><svg width="11" height="11" viewBox="0 0 12 12"><path d="M3 1 5 3.5 4 5a7 7 0 0 0 3 3l1.5-1L11 9l-1 2C5 11 1 7 1 2z" fill="#0677ba"/></svg></span>02 5550 1234</div>
    <div class="row"><span class="ico"><svg width="10" height="12" viewBox="0 0 10 12"><path d="M5 11S1 6.5 1 4a4 4 0 0 1 8 0c0 2.5-4 7-4 7z" fill="#0677ba"/><circle cx="5" cy="4" r="1.5" fill="#fff"/></svg></span>Sydney NSW, Australia</div>
    <div class="row"><span class="ico"><svg width="11" height="9" viewBox="0 0 11 9" fill="none" stroke="#0677ba" stroke-width="1.4"><rect x=".7" y=".7" width="9.6" height="7.6"/><path d="m1 1 4.5 4L10 1"/></svg></span>info@brindovasolutions.com.au</div>
  </div>
  <div class="abs rule"></div>
  <p class="abs legal" style="left:56px">© Copyright 2021 Brindova Electrical Solutions | All Rights Reserved</p>
  <p class="abs legal" style="right:57px">Privacy Policy</p>
</footer>

</body>
</html>
```